Pharmacist turned chef in Key West Fl needs a logo design

I am looking for a professional looking business card that says who I am and what I do. For example Chef Dale Morvik, natural organic and health supportive cooking. Phone 555-416-8870 email dalemorvik@quillpost.example web www.thesaltedharvest.example, Key West fl. The color or colors should have some green and other colors that look good together that stimulate appetite and give a clean healthy image. To help with a thought process, words like food as medicine, medicine is food, good nutrition is health but at the same time I do not want a lot of medical symbols that me it look clinical. Any questions please contact me.

```html
<!DOCTYPE html>
<html lang="en">
<head>
<meta charset="utf-8">
<title>Chef Dale Morvik – Business Card</title>
<link rel="stylesheet" href="https://fonts.googleapis.com/css2?family=Open+Sans:wght@400;600;700&display=swap">
<style>
  :root {
    --bg: #e4e5e7;
    --card: #f7f8f6;
    --ink: #2b2b2b;
    --band-dark: #3c8a3a;
    --band-mid: #4f9f45;
    --band-light: #76b957;
    --band-pale: #9fd07a;
    --white: #ffffff;
  }
  * { box-sizing: border-box; margin: 0; padding: 0; }
  html, body { width: 1200px; height: 883px; overflow: hidden; }
  body {
    background: var(--bg);
    font-family: "Open Sans", Arial, sans-serif;
    color: var(--ink);
    position: relative;
  }
  .card {
    position: absolute;
    width: 520px;
    height: 300px;
    background: var(--card);
    border-radius: 26px;
    overflow: hidden;
    box-shadow: 0 6px 18px rgba(0,0,0,0.12);
  }
  .card--front { left: 50px; top: 292px; }
  .card--back  { left: 630px; top: 292px; }

  /* Front */
  .front__name {
    position: absolute; top: 42px; left: 0; right: 0;
    text-align: center; font-size: 31px; font-weight: 400; letter-spacing: -0.3px;
  }
  .front__name strong { font-weight: 700; }
  .front__tagline {
    position: absolute; top: 86px; left: 0; right: 0;
    text-align: center; font-size: 15px; font-weight: 400;
  }
  .front__tagline strong { font-weight: 700; }
  .front__band {
    position: absolute; top: 124px; left: 0; right: 0; height: 96px;
    background: linear-gradient(100deg,
      var(--band-pale) 0, var(--band-pale) 20px,
      var(--band-dark) 20px, var(--band-dark) 262px,
      var(--band-mid) 262px, var(--band-mid) 292px,
      var(--band-light) 292px, var(--band-light) 100%);
  }
  .band__phone {
    position: absolute; left: 62px; top: 28px;
    color: var(--white); font-size: 15px; line-height: 20px;
  }
  .band__web {
    position: absolute; left: 290px; right: 14px; top: 20px; text-align: center;
    color: var(--white); font-size: 13px; line-height: 19px;
  }
  .band__label { text-transform: uppercase; }
  .front__address {
    position: absolute; top: 240px; left: 0; right: 0;
    text-align: center; font-size: 13px; line-height: 17px; text-transform: uppercase;
  }
  .front__address strong { font-weight: 700; }

  /* Back */
  .back__band {
    position: absolute; top: 100px; left: 0; right: 0; height: 98px;
    background: linear-gradient(100deg,
      var(--band-pale) 0, var(--band-light) 100px,
      var(--band-dark) 100px, var(--band-mid) 420px,
      var(--band-pale) 420px, var(--band-light) 100%);
    display: flex; align-items: center; justify-content: center;
  }
  .back__web {
    color: var(--white); font-size: 15px; font-weight: 600; letter-spacing: 3px;
    text-transform: uppercase;
  }
</style>
</head>
<body>
  <section class="card card--front" aria-label="Business card front">
    <h1 class="front__name">Chef Dale <strong>Morvik</strong></h1>
    <p class="front__tagline"><strong>Natural Organic</strong> &amp; Health Supportive Cooking</p>
    <div class="front__band">
      <p class="band__phone"><span class="band__label">Phone</span><br>555-416-8870</p>
      <p class="band__web"><span class="band__label">Email &amp; Web</span><br>dalemorvik@quillpost.example<br>www.thesaltedharvest.example</p>
    </div>
    <p class="front__address"><strong>Key West</strong>, <strong>Florida</strong><br>United States</p>
  </section>

  <section class="card card--back" aria-label="Business card back">
    <div class="back__band">
      <p class="back__web">www.thesaltedharvest.example</p>
    </div>
  </section>
</body>
</html>
```